International Luxury Furniture and Accessories Outsourcing Company

We Need a Business Card design for a new Outsourcing company doing Business Internationally in the Luxury Furniture and Accessories Space. The company's name is MARCUS BELLWOOD and we deal with clients in the high end and Luxury Space for Furniture and Accessories in the world. We would like Designs that speaks Luxury and Professionalism.

We like the Combination of the color Brown and Gold or Black and Gold. We are also open to other color combo.

We like some of the design of file attached.
Updates

This is Peter and We really appreciate all of you taking the time out and putting the effort to help us jump start our new company. We have 2-3 designs that we like and will decide soon to pick one. Once again, Thank you to all of you !! Best Regards, Peter

Industry/Entity Type

Business

```html
<!DOCTYPE html>
<html lang="en">
<head>
<meta charset="UTF-8">
<title>Marcus Bellwood – Business Card</title>
<link href="https://fonts.googleapis.com/css2?family=Oranienbaum&family=Cinzel:wght@400&family=Titillium+Web:wght@300;400&display=swap" rel="stylesheet">
<style>
  :root {
    --page: #ffffff;
    --card: #3d3d3b;
    --card-edge: #8a8a88;
    --gold: #f39200;
    --ink: #ffffff;
  }
  * { margin: 0; padding: 0; box-sizing: border-box; }
  html, body {
    width: 1200px; height: 1000px; overflow: hidden;
    background: var(--page);
  }
  .canvas { position: relative; width: 1200px; height: 1000px; }
  .card {
    position: absolute;
    background: var(--card);
    color: var(--ink);
  }
  .card--front { left: 234px; top: 55px; width: 708px; height: 425px; }
  .card--back {
    left: 233px; top: 517px; width: 710px; height: 427px;
    border-right: 3px solid var(--card-edge);
  }

  /* Front */
  .brand-mark {
    position: absolute; left: 313px; top: 125px;
    width: 70px; height: 70px; border-radius: 50%;
    background: var(--gold);
  }
  .brand-name {
    position: absolute; left: 0; right: 0; top: 247px;
    text-align: center;
    font-family: "Oranienbaum", serif;
    font-size: 36px; letter-spacing: 1px; line-height: 1;
    color: var(--ink);
  }
  .brand-tagline {
    position: absolute; left: 0; right: 0; top: 293px;
    text-align: center;
    font-family: "Cinzel", serif;
    font-size: 13px; letter-spacing: 0.6px; line-height: 1;
    color: var(--ink);
  }

  /* Back */
  .back-brand {
    position: absolute; left: 54px; top: 78px;
    font-family: "Titillium Web", sans-serif; font-weight: 400;
    font-size: 15px; letter-spacing: 1px; line-height: 1;
    color: var(--ink);
  }
  .holder {
    position: absolute; right: 50px; top: 50px; text-align: right;
    font-family: "Titillium Web", sans-serif; font-weight: 300;
    line-height: 1.05;
  }
  .holder__name { font-size: 27px; font-weight: 400; }
  .holder__role { font-size: 21px; }
  .contact-list {
    position: absolute; top: 253px; list-style: none;
    font-family: "Titillium Web", sans-serif; font-weight: 300;
    font-size: 19px; line-height: 22px; letter-spacing: -0.3px;
  }
  .contact-list--address { left: 62px; }
  .contact-list--reach { left: 513px; }
</style>
</head>
<body>
<main class="canvas">
  <section class="card card--front">
    <div class="brand-mark" aria-hidden="true"></div>
    <h1 class="brand-name">MARCUS BELLWOOD</h1>
    <p class="brand-tagline">LUXURY FURNITURE AND ACCESSORIES</p>
  </section>

  <section class="card card--back">
    <div class="back-brand">MARCUS BELLWOOD</div>
    <div class="holder">
      <div class="holder__name">PERSON NAME</div>
      <div class="holder__role">DESIGNATION</div>
    </div>
    <ul class="contact-list contact-list--address">
      <li>0000 Street Name</li>
      <li>Building Name</li>
      <li>Blcok No</li>
      <li>City, Zip Code</li>
      <li>Country</li>
    </ul>
    <ul class="contact-list contact-list--reach">
      <li>+1 123 456 7890</li>
      <li>facebook/id</li>
      <li>twitter/id</li>
      <li>info@domain.com</li>
      <li>www.domain.com</li>
    </ul>
  </section>
</main>
</body>
</html>
```